Business Card and Word .doc header and footer required

I need a business card designed for my cybersecurity consulting company. Also required, is a header and footer to be ued for my word documents.
Attached is the Logo design, font and rgb used.

Industry/Entity Type

Cyber Security Consulting

Contact Information for Business Card

Name, Phone, email, website

Colors
0054AA
0677BA
7BADD7
CADEEF
E8F1F8

Requirements
Must have
• Sleek, modern

```html
<!DOCTYPE html>
<html lang="en">
<head>
<meta charset="utf-8">
<title>Harbor Vale Consulting – Business Card</title>
<link rel="stylesheet" href="https://fonts.googleapis.com/css2?family=Lexend:wght@400;500;600;700&display=swap">
<style>
  :root {
    --bg: #1f1f21;
    --card-white: #ffffff;
    --navy: #15203f;
    --brand-blue: #0a6ea6;
    --back-blue: #0e78ad;
    --back-blue-dark: #0a6392;
    --rule: #9a9a9a;
    --ink: #1a1a1a;
  }
  * { box-sizing: border-box; margin: 0; padding: 0; }
  html, body { width: 1200px; height: 1108px; overflow: hidden; }
  body {
    background: var(--bg);
    font-family: "Lexend", sans-serif;
    position: relative;
  }
  .card {
    position: absolute;
    top: 164px;
    width: 460px;
    height: 780px;
    border-radius: 30px;
    overflow: hidden;
  }
  .card-front {
    left: 120px;
    background: var(--card-white);
    text-align: center;
    padding-top: 118px;
  }
  .card-back {
    left: 620px;
    background: var(--back-blue);
  }
  .brand-mark {
    width: 120px; height: 120px;
    border: 10px solid var(--brand-blue);
    border-radius: 50%;
    margin: 0 auto 26px;
  }
  .brand-name {
    color: var(--navy);
    font-weight: 700;
    font-size: 46px;
    letter-spacing: 1px;
    line-height: 1;
  }
  .brand-tagline {
    display: flex; align-items: center; justify-content: center; gap: 10px;
    color: var(--brand-blue);
    font-size: 18px; letter-spacing: 9px;
    margin-top: 10px;
  }
  .brand-tagline::before, .brand-tagline::after {
    content: ""; width: 30px; height: 2px; background: var(--brand-blue);
  }
  .person-name {
    margin-top: 58px;
    color: var(--navy);
    font-weight: 700; font-size: 28px; letter-spacing: 1px;
  }
  .person-title {
    color: var(--brand-blue);
    font-size: 21px; letter-spacing: 1px;
    margin-top: 2px;
  }
  .icon-row {
    display: flex; align-items: center; justify-content: center; gap: 8px;
    margin: 22px 40px 12px;
  }
  .icon-row::before, .icon-row::after {
    content: ""; flex: 1; height: 1px; background: var(--rule);
  }
  .icon {
    width: 36px; height: 36px; border-radius: 6px;
    background: var(--brand-blue);
    display: flex; align-items: center; justify-content: center;
  }
  .contact-list { list-style: none; color: var(--ink); font-size: 22px; line-height: 1.35; }
  .contact-list .accent { color: var(--brand-blue); }
  .divider { height: 1px; background: var(--rule); margin: 14px 40px 16px; }
  .address { font-style: normal; color: var(--ink); font-size: 21px; line-height: 1.35; }
  .back-pattern {
    position: absolute; inset: 0;
    background: radial-gradient(circle at 75% 20%, #1596d2 0%, var(--back-blue) 45%, var(--back-blue-dark) 100%);
  }
  .back-mark {
    position: absolute; left: 316px; top: 560px;
    display: flex; align-items: center; gap: 8px;
    color: #ffffff; font-size: 15px; font-weight: 600;
  }
  .back-mark::before {
    content: ""; width: 30px; height: 30px; border: 3px solid #ffffff; border-radius: 50%;
  }
</style>
</head>
<body>
  <section class="card card-front" aria-label="Business card front">
    <div class="brand-mark"></div>
    <div class="brand-name">HARBOR VALE</div>
    <div class="brand-tagline">CONSULTING</div>

    <div class="person-name">DANIEL BROOKS</div>
    <div class="person-title">MANAGING DIRECTOR</div>

    <div class="icon-row">
      <span class="icon" aria-label="Phone">
        <svg width="22" height="22" viewBox="0 0 24 24"><path fill="#fff" d="M6.6 10.8a15 15 0 0 0 6.6 6.6l2.2-2.2c.3-.3.7-.4 1-.2 1.1.4 2.3.6 3.6.6.6 0 1 .4 1 1V20c0 .6-.4 1-1 1A17 17 0 0 1 3 4c0-.6.4-1 1-1h3.5c.6 0 1 .4 1 1 0 1.3.2 2.5.6 3.6.1.3 0 .7-.2 1z"/></svg>
      </span>
      <span class="icon" aria-label="Email">
        <svg width="22" height="22" viewBox="0 0 24 24"><rect x="3" y="5" width="18" height="14" rx="1.5" fill="none" stroke="#fff" stroke-width="2"/><path d="M3 6l9 7 9-7" fill="none" stroke="#fff" stroke-width="2"/></svg>
      </span>
      <span class="icon" aria-label="Website">
        <svg width="22" height="22" viewBox="0 0 24 24"><circle cx="12" cy="12" r="9" fill="none" stroke="#fff" stroke-width="2"/><path d="M3 12h18M12 3c3 3 3 15 0 18M12 3c-3 3-3 15 0 18" fill="none" stroke="#fff" stroke-width="1.6"/></svg>
      </span>
    </div>

    <ul class="contact-list">
      <li>044-555 010 234</li>
      <li>hello@harborvale.com</li>
      <li>www.<span class="accent">harborvale</span>.com</li>
    </ul>

    <div class="divider"></div>

    <address class="address">88, Quayside Road, Suite 4<br>30117, Northland</address>
  </section>

  <section class="card card-back" aria-label="Business card back">
    <div class="back-pattern" role="img" aria-label="Embossed repeating brand-symbol pattern on blue"></div>
    <div class="back-mark">Harbor Vale</div>
  </section>
</body>
</html>
```